Flyer for local business that installs fences and sells fence materials

We recently began selling fence materials, in addition to also doing fence installations. We need a flyer that displays our business information and photos of our work, as well as a flyer that shows customers they have the option to buy materials only also.

If they are looking to build a fence - we can help by installing it, or if they want to install themselves, they can buy the materials only from us too. We provide a lifetime warranty on all materials and installations. More information about the company is here: www.BrambleRailWorks.com

Its important to have the company logo, phone number, email and business hours listed (Monday - Thursday 9AM - 3PM, Friday 9AM - 1PM).

It is also important to show the fence material types we offer:
Wood, Chainlink, Vinyl and Aluminum
Updates

Updated with more photos and url to website www.bramblerailworks.com for details

Target Market(s)

Residential Homeowners

Industry/Entity Type

Construction

Font styles to use
Sans Serif
Other font styles liked:
• Arial

Colors
0054AA
0677BA
7BADD7
CADEEF
E8F1F8

Requirements
Must have
• Photos of the fencing we offer
Nice to have
• A way to explain to customers they can hire us to install, or just buy the materials from us
Should not have
• Too many colors or too many words

```html
<!DOCTYPE html>
<html lang="en">
<head>
<meta charset="utf-8">
<title>Bramble Rail Works – Fence Installation &amp; Materials</title>
<link href="https://fonts.googleapis.com/css2?family=Oswald:wght@500;600&family=Roboto:wght@400;700;900&display=swap" rel="stylesheet">
<style>
  :root {
    --sky-top: #a9b0b7;
    --sky-bottom: #e8eaed;
    --wood-light: #e3c597;
    --wood-dark: #c89f69;
    --brand-orange: #e07f22;
    --ink: #1d1d1d;
    --ink-soft: #333333;
    --accent-red: #c7261c;
    --frame: #ffffff;
  }
  * { margin: 0; padding: 0; box-sizing: border-box; }
  html, body { width: 849px; height: 1200px; overflow: hidden; background: #ffffff; }
  .flyer {
    position: relative;
    width: 849px;
    height: 1200px;
    overflow: hidden;
    font-family: "Roboto", Arial, sans-serif;
    color: var(--ink);
  }
  .backdrop { position: absolute; inset: 0; width: 849px; height: 1200px; }

  .brand { position: absolute; left: 508px; top: 34px; }
  .brand-mark {
    position: absolute; left: 0; top: 4px;
    width: 52px; height: 52px;
    background: var(--ink-soft);
  }
  .brand-name {
    position: absolute; left: 66px; top: 0;
    font-weight: 700; font-size: 27px; line-height: 30px;
    color: var(--brand-orange); white-space: nowrap;
  }
  .brand-phone {
    position: absolute; left: 66px; top: 30px;
    font-weight: 900; font-size: 30px; line-height: 32px;
    color: var(--ink); white-space: nowrap;
  }
  .brand-tagline {
    position: absolute; left: 66px; top: 64px;
    font-weight: 700; font-size: 11.5px; font-style: italic;
    color: var(--ink-soft); white-space: nowrap;
  }

  .contact { position: absolute; left: 508px; top: 150px; color: var(--ink-soft); }
  .contact-email { font-size: 20px; line-height: 26px; margin-bottom: 10px; }
  .contact-hours { font-size: 19px; line-height: 24px; }

  .gallery { position: absolute; left: 84px; top: 252px; }
  .gallery-photo {
    position: absolute;
    width: 146px;
    border: 6px solid var(--frame);
    box-shadow: 4px 6px 14px rgba(0,0,0,0.35);
  }
  .photo-wood   { top: 0;   height: 200px; background: linear-gradient(160deg, #5b5248, #c9a26e 45%, #8a6a44); }
  .photo-chain  { top: 244px; height: 196px; background: linear-gradient(180deg, #b9c9d6 0%, #8fa06b 45%, #6f7f55 70%, #9b9a92 100%); }
  .photo-vinyl  { top: 472px; height: 212px; background: linear-gradient(170deg, #aeb7c2, #e9e4da 50%, #c3b69f); }
  .photo-alum   { top: 712px; height: 196px; background: linear-gradient(180deg, #3d77c4 0%, #8fb3de 45%, #f1f1ef 60%, #b88a5a 100%); }

  .headline {
    position: absolute; right: 30px; top: 640px;
    text-align: right;
    font-family: "Oswald", "Arial Narrow", sans-serif;
    font-weight: 600; text-transform: uppercase;
    font-size: 72px; line-height: 76px;
    color: var(--ink);
  }
  .headline-or { color: var(--accent-red); font-size: 78px; line-height: 86px; }
</style>
</head>
<body>
<main class="flyer">
  <svg class="backdrop" viewBox="0 0 849 1200" aria-hidden="false">
    <defs>
      <linearGradient id="sky" x1="0" y1="0" x2="0" y2="1">
        <stop offset="0" stop-color="var(--sky-top)"/>
        <stop offset="1" stop-color="var(--sky-bottom)"/>
      </linearGradient>
      <linearGradient id="wood" x1="0" y1="0" x2="1" y2="0">
        <stop offset="0" stop-color="var(--wood-dark)"/>
        <stop offset="0.5" stop-color="var(--wood-light)"/>
        <stop offset="1" stop-color="var(--wood-dark)"/>
      </linearGradient>
    </defs>
    <rect role="img" aria-label="Cloudy grey sky behind the fence" x="0" y="0" width="849" height="1200" fill="url(#sky)"/>
    <path role="img" aria-label="Close view of a new wooden picket fence" fill="url(#wood)"
      d="M0 0 L60 8 Q240 40 400 150 Q620 300 849 640 L849 1200 L0 1200 Z"/>
  </svg>

  <header class="brand">
    <div class="brand-mark"></div>
    <div class="brand-name">Bramble Rail Works</div>
    <div class="brand-phone">704-555-0142</div>
    <div class="brand-tagline">"Because Good Fences Make Good Neighbors"</div>
  </header>

  <section class="contact">
    <p class="contact-email">office@bramblerailworks.com</p>
    <p class="contact-hours">Monday - Thursday 9AM - 3PM,<br>Friday 9AM - 1PM</p>
  </section>

  <section class="gallery">
    <div class="gallery-photo photo-wood" role="img" aria-label="Photo of an installed wood privacy fence"></div>
    <div class="gallery-photo photo-chain" role="img" aria-label="Photo of a chainlink fence along a yard"></div>
    <div class="gallery-photo photo-vinyl" role="img" aria-label="Photo of stacked fence materials ready for pickup"></div>
    <div class="gallery-photo photo-alum" role="img" aria-label="Photo of a white vinyl fence under blue sky"></div>
  </section>

  <h1 class="headline">
    Hire us<br>to install<br>
    <span class="headline-or">or</span><br>
    just buy<br>the materials<br>from us
  </h1>
</main>
</body>
</html>
```